lumbrett-scope virtual tours is looking for a website redisgn that uses our new logo

Using LBS's logo as a basis, please redesign our website. Our web application developer has a stand-in site up at www.lb-scope.net. LBS is a virtual tour company whose main clients are the owners of real estate and rental properties; however, LBS will produce virtual tours for any person, company, or organization for whatever purpose they see fit to use the tour for. This is a dynamic website consisting of three pages. An index/info page, a contact/web form page, a price listing page, a template for a tour page which will have a height/width 75% iframe that showcases one of our tours (www.lb-scope.net) for an example. What is needed: HTML template design for pages that incorporates logo, custom graphic for mail link, FB link, Twitter link, and Virtual Tour link. We would also like a watermarked developed out of our logo pin (.ai of logo pin included). The watermark should also include the capital letters LBS, be in grayscale, translucent and the masked.
Target Market(s)
Home Owners, Real Estate Agents, Property Managers, Event Managers, Business Owners, Park Owners,
Industry/Entity Type
Real Estate
Number of Pages Required
3 page
Requirements
Must have
- New web design that uses our logo (file included). Must have a custom watermark that uses our custom logo pin (file included). Watermark should be gray scale, translucent, and masked. Custom graphics for homepage link (would like something that uses our logo pin), mail link, facebook link, and twitter link.
Nice to have
- I've uploaded a pdf called pano_vs_spherical.pdf which is a scan of a crude drawing I did that illustrates what we'd like for our info page. Basically we'd like to describe the difference between a panoramic image and a spherical image and to do so we'd like to have some graphical drawings that illustrate which each is. We'd like two separate image files that we can include on our info page. Use the uploaded .pdf as a guide. Would also like images 0-9 of custom numerals that match the theme of the page to be used as part of a visitor counter script.
Should not have
- Do not need html code or stylesheets (css). Would rather you concentrate on graphic design of custom graphics, layout, and color scheme. We have competent web applications developers in our small company who can code, we just need you, the graphic artist to work your magic.

```html
<!DOCTYPE html>
<html lang="en">
<head>
<meta charset="utf-8">
<title>lumbrett-scope virtual tours</title>
<link href="https://fonts.googleapis.com/css2?family=Open+Sans:wght@400;600;700&family=Oswald:wght@400;500&family=Montserrat:wght@500;600&display=swap" rel="stylesheet">
<style>
:root{
  --orange:#f17a25;
  --orange-light:#f5a04e;
  --orange-dark:#e0661a;
  --ink:#333333;
  --text:#666666;
  --page:#f7f7f7;
  --black:#000000;
  --bar:#333333;
  --white:#ffffff;
}
*{margin:0;padding:0;box-sizing:border-box}
h1,h2,h3,h4{font-weight:400}
html,body{width:749px;height:1200px;overflow:hidden}
body{position:relative;background:var(--page);font-family:"Open Sans",Arial,sans-serif;color:var(--text)}
.abs{position:absolute}
.top-bg{left:0;top:0;width:749px;height:440px;background:linear-gradient(#ffffff,#e9e9e9 70%,#d7d7d7)}
.brand{left:55px;top:14px;display:flex;align-items:center;gap:7px}
.brand-dot{width:20px;height:20px;border-radius:50%;background:var(--orange)}
.brand-name{font-size:19px;font-weight:600;color:var(--ink);letter-spacing:-.3px}
.brand-tag{left:82px;top:40px;font-size:6px;font-weight:600;color:var(--ink);letter-spacing:.5px;text-transform:uppercase}
.phone{left:490px;top:28px;display:flex;align-items:center;gap:6px;font-size:13px;color:var(--ink)}
.social{top:27px;width:18px;height:18px;border-radius:50%;box-shadow:0 1px 2px rgba(0,0,0,.3)}
.nav{left:55px;top:68px;width:639px;height:38px;background:linear-gradient(var(--orange-light),var(--orange));display:flex}
.nav a{color:var(--white);text-decoration:none;font-size:10.5px;line-height:38px;text-align:center;border-right:1px solid rgba(255,255,255,.25);text-transform:uppercase}
.nav a.current{background:linear-gradient(#444,#222)}
.hero{left:55px;top:106px;width:639px;height:334px;background:linear-gradient(180deg,#4d6fa8 0%,#9eb6d6 35%,#c9b8a4 55%,#5e6e3a 75%,#3a6e8e 100%)}
.caption{left:55px;top:234px;width:230px;height:96px;background:rgba(40,40,40,.45)}
.hero-title{left:73px;top:244px;font-family:"Oswald",sans-serif;font-size:32px;color:var(--white);letter-spacing:-.5px}
.hero-sub{left:74px;top:286px;font-size:13px;color:var(--white)}
.arrow{top:408px;width:18px;height:18px}
.welcome{left:0;top:472px;width:749px;text-align:center;font-family:"Montserrat",sans-serif;font-weight:600;font-size:15px;color:var(--ink)}
.welcome span{color:var(--orange)}
.intro{left:52px;top:499px;width:645px;text-align:center;font-size:7.4px;line-height:13.3px;color:var(--text);letter-spacing:-.05px}
.btn{left:342px;top:552px;width:65px;height:21px;border-radius:3px;background:linear-gradient(var(--orange-light),var(--orange-dark));color:var(--white);font-size:8.5px;text-align:center;line-height:21px}
.band{left:0;top:595px;width:749px;height:253px;background:var(--orange)}
.band-title{left:55px;top:616px;font-size:13px;font-weight:600;color:var(--white)}
.circle-arrow{top:616px;width:17px;height:17px}
.card{top:644px;width:155px;height:175px;background:var(--white);box-shadow:0 6px 8px -4px rgba(0,0,0,.35)}
.card-photo{width:155px;height:106px}
.card-title{margin:14px 10px 0;font-size:9px;color:var(--orange);text-transform:uppercase}
.card-text{margin:3px 10px 0;font-size:7.5px;line-height:12px;color:var(--text)}
.feature-img{background:linear-gradient(#ffffff,#f0f0f0);border:1px solid #eee}
.feature-title{font-size:10.5px;color:var(--orange);text-transform:uppercase}
.feature-text{font-size:7px;line-height:13px;color:var(--text)}
.outline-btn{height:19px;border:1px solid #bbb;border-radius:3px;background:var(--white);font-size:7px;color:var(--ink);text-align:center;line-height:17px}
.footer{left:0;top:1013px;width:749px;height:140px;background:var(--black)}
.f-head{font-size:10.5px;color:var(--white);text-transform:uppercase}
.f-text{font-size:7.5px;line-height:13px;color:var(--white)}
.email-field{left:268px;top:1093px;width:119px;height:28px;border:1px solid #999;background:var(--black);color:#ccc;font-size:7px;line-height:26px;padding-left:6px}
.signup{left:387px;top:1093px;width:46px;height:28px;background:var(--orange);color:var(--white);font-size:10px;text-align:center;line-height:28px}
.map{left:520px;top:1015px;width:160px;height:138px;background:radial-gradient(circle at 50% 45%,#f5b870,#e9e3d0 45%,#f3f3f3)}
.bottom{left:0;top:1153px;width:749px;height:47px;background:var(--bar)}
.copy{left:54px;top:1172px;font-size:7px;color:var(--white)}
.follow{left:577px;top:1170px;font-size:9px;font-weight:600;color:var(--white)}
.foot-social{top:1167px;width:16px;height:16px;border:1px solid #ddd;border-radius:50%}
</style>
</head>
<body>
<div class="abs top-bg"></div>

<header>
  <div class="abs brand"><span class="brand-dot"></span><span class="brand-name">lumbrett-scope</span></div>
  <div class="abs brand-tag">virtual tours</div>
  <div class="abs phone">
    <svg width="11" height="11" viewBox="0 0 11 11"><rect width="11" height="11" rx="2" fill="#f17a25"/><path d="M3 2.5l1.4 1.6-.7.9c.5 1 1.3 1.8 2.3 2.3l.9-.7L8.5 8l-.8.9C5 8.6 2.4 6 2.1 3.3z" fill="#fff"/></svg>
    <span>555.018.4420</span>
  </div>
  <span class="abs social" style="left:607px;background:#3b5a9a"></span>
  <span class="abs social" style="left:629px;background:#d84b37"></span>
  <span class="abs social" style="left:651px;background:#2aa3dc"></span>
  <span class="abs social" style="left:673px;background:#f26522"></span>
  <nav class="abs nav">
    <a class="current" style="width:67px">Home</a>
    <a style="width:87px">About Us</a>
    <a style="width:82px">Services</a>
    <a style="width:64px">Blog</a>
    <a style="width:65px">News</a>
    <a style="width:82px">Contact</a>
    <a style="width:67px">Prices</a>
  </nav>
</header>

<section>
  <div class="abs hero" role="img" aria-label="Modern villa with pool and palm trees at dusk"></div>
  <div class="abs caption"></div>
  <div class="abs hero-title">LUMBRETT-SCOPE</div>
  <div class="abs hero-sub">Click Here for fullscreen View</div>
  <svg class="abs arrow" style="left:648px" viewBox="0 0 18 18"><rect width="18" height="18" fill="#f17a25"/><path d="M10.5 5.5L7 9l3.5 3.5" stroke="#fff" stroke-width="1.6" fill="none"/></svg>
  <svg class="abs arrow" style="left:665px" viewBox="0 0 18 18"><rect width="18" height="18" fill="#333"/><path d="M7.5 5.5L11 9l-3.5 3.5" stroke="#fff" stroke-width="1.6" fill="none"/></svg>
</section>

<section>
  <h1 class="abs welcome">WELCOME TO <span>LUMBRETT-SCOPE</span></h1>
  <p class="abs intro">Lorem Ipsum has been the industry's standard dummy text ever since the 1500s, when an unknown printer took a galley of type and scrambled it to make a type specimen book. It has survived not only five centuries, but also the leap into electronic typesetting, remaining essentially unchanged. It was popularised in the 1960s with the release of Lindqvar sheets containing Lorem Ipsum passages, and more recently with desktop publishing software like Brightfold PageSetter including versions of Lorem Ipsum.</p>
  <div class="abs btn">Read More</div>
</section>

<section>
  <div class="abs band"></div>
  <h2 class="abs band-title">PROPERTIES</h2>
  <svg class="abs circle-arrow" style="left:655px" viewBox="0 0 17 17"><circle cx="8.5" cy="8.5" r="7.7" stroke="#fff" stroke-width="1.3" fill="none"/><path d="M9.8 5.5L6.8 8.5l3 3" stroke="#fff" stroke-width="1.5" fill="none"/></svg>
  <svg class="abs circle-arrow" style="left:676px" viewBox="0 0 17 17"><circle cx="8.5" cy="8.5" r="7.7" stroke="#fff" stroke-width="1.3" fill="none"/><path d="M7.2 5.5l3 3-3 3" stroke="#fff" stroke-width="1.5" fill="none"/></svg>
  <article class="abs card" style="left:54px"><div class="card-photo" role="img" aria-label="Suburban family house with lawn" style="background:linear-gradient(#4a78c0,#9fb7d8 45%,#8a6a55 60%,#5c8a3c)"></div><h3 class="card-title">Ipsum is simply dummy</h3><p class="card-text">Lorem Ipsum is simply dummy text of the printing and typesetting industry</p></article>
  <article class="abs card" style="left:216px"><div class="card-photo" role="img" aria-label="Modern white house with garage" style="background:linear-gradient(#3f7fd0,#a9c6e8 40%,#e2e2e2 60%,#8a8a8a)"></div><h3 class="card-title">Ipsum is simply dummy</h3><p class="card-text">Lorem Ipsum is simply dummy text of the printing and typesetting industry</p></article>
  <article class="abs card" style="left:378px"><div class="card-photo" role="img" aria-label="Lit modern home with pool at night" style="background:linear-gradient(#2c3e55,#5b6778 40%,#c9a878 65%,#1d5a8a)"></div><h3 class="card-title">Ipsum is simply dummy</h3><p class="card-text">Lorem Ipsum is simply dummy text of the printing and typesetting industry</p></article>
  <article class="abs card" style="left:540px"><div class="card-photo" role="img" aria-label="Stucco building with tall windows" style="background:linear-gradient(#23428a,#4d6fb2 35%,#e6dccb 60%,#b9a58c)"></div><h3 class="card-title">Ipsum is simply dummy</h3><p class="card-text">Lorem Ipsum is simply dummy text of the printing and typesetting industry</p></article>
</section>

<section>
  <div class="abs feature-img" role="img" aria-label="Sketch of a spherical image" style="left:50px;top:890px;width:84px;height:85px"></div>
  <h3 class="abs feature-title" style="left:139px;top:890px">Spherical</h3>
  <p class="abs feature-text" style="left:138px;top:907px;width:215px">Lorem Ipsum has been the industry's standard dummy text ever since the 1500s, when an unknown printer took a galley of type andonly five centuries, but also the leap into electronic typeset-ting,</p>
  <div class="abs outline-btn" style="left:140px;top:964px;width:59px">READ MORE</div>

  <div class="abs feature-img" role="img" aria-label="Sketch of a camera on a tripod capturing a panoramic image" style="left:362px;top:876px;width:111px;height:96px"></div>
  <h3 class="abs feature-title" style="left:478px;top:883px">Panoramic</h3>
  <p class="abs feature-text" style="left:475px;top:900px;width:225px">Lorem Ipsum has been the industry's standard dummy text ever since the 1500s, when an unknown printer took a galley of type andonly five centuries, but also the leap into electronic typesetting, remaining essentially unchanged. It was popularised</p>
  <div class="abs outline-btn" style="left:477px;top:957px;width:59px">READ MORE</div>
</section>

<footer>
  <div class="abs footer"></div>
  <h4 class="abs f-head" style="left:54px;top:1031px">Address</h4>
  <p class="abs f-text" style="left:55px;top:1053px">HALVORSEN ALLEE 12 · 30419<br>Marlbrück DE</p>
  <h4 class="abs f-head" style="left:56px;top:1085px;font-size:9.5px">Telephone</h4>
  <p class="abs f-text" style="left:57px;top:1102px;font-size:8px;line-height:16px">+ 49 000. 555 017 42 ·<br>hello@lb-scope.net</p>
  <h4 class="abs f-head" style="left:268px;top:1031px">Newsletter</h4>
  <p class="abs f-text" style="left:268px;top:1053px;width:180px;font-size:6.5px;line-height:12px">Excepteur sint occaecat cupidatat non proident, sunt in culpa qui officia deserunt mollit anim id est laborum.</p>
  <div class="abs email-field">Enter Email</div>
  <div class="abs signup">Sign Up</div>
  <div class="abs map" role="img" aria-label="Magnifying glass over a street map with location pin"></div>
  <div class="abs bottom"></div>
  <p class="abs copy">© 2015 . All rights reserved.</p>
  <p class="abs follow">Follow us :</p>
  <span class="abs foot-social" style="left:632px"></span>
  <span class="abs foot-social" style="left:654px"></span>
  <span class="abs foot-social" style="left:676px"></span>
</footer>
</body>
</html>
```